Private practice for psychiatry and psychotherapy needs a business card and logo

I need a logo and business card design for my private practice for psychiatry and psychotherapy. The optional names for my practice are: Voskuilen Praktijk voor Psychiatrie en Psychotherapie, or short: Praktijk Voskuilen.
I am a (child and adolescent) psychiatrist and psychotherapist. I diagnose and treat infants, children, adolescents and adults with psychiatric symptoms/disorders. I also give supervision to colleagues about their own treatments. My work is characterised by personal involvement, transparence, creativity and professionality.
I would like to have an appealing, light and bright, yet basic design that invites people (both children and adults) to contact me, gives trust and hope, without loosing professional appearance.
I uploaded my contact information which should not necessarily be all included (in this form) on the card as long as people know how to contact me. Please feel free to be creative!
Please note that my website is only temporarely and need a new design and update too!

Target Market(s)

Clients and patients (children, adolescents, adults) with psychiatric symptoms who need diagnosis and treatment. I work with private clients and patients through medical insurances.

Industry/Entity Type

Mental Health

Contact Information for Business Card

Dr. Femke Voskuilen-ter Horst
Psychiater/Kinder- en Jeugdpsychiater
Gerrit Wassinkstraat 4
3063 TW Rotterdam
t: 06-58190274
e: info@praktijkvoskuilen-voorbeeld.nl
i: www.praktijkvoskuilen-voorbeeld.nl

Logo Text

Praktijk Voskuilen voor Psychiatrie en Psychotherapie; or short: Praktijk Voskuilen

Font styles to use
Sans Serif
Other font styles liked:
• up to designer

Requirements
Must have
• Appealing, light, bright, creative, trustful, professional and unique.

```html
<!DOCTYPE html>
<html lang="nl">
<head>
<meta charset="utf-8">
<title>Praktijk Voskuilen – visitekaartje</title>
<link rel="stylesheet" href="https://fonts.googleapis.com/css2?family=Carlito:wght@400;700&family=Exo+2:wght@700&display=swap">
<style>
  :root {
    --stage: #000000;
    --paper: #ffffff;
    --brand-blue: #1f6cae;
    --brand-blue-light: #2b80c2;
    --brand-blue-dark: #1d63a3;
    --text-grey: #4a4a4a;
    --soft-blue: rgba(120, 165, 205, 0.35);
    --soft-white: rgba(255, 255, 255, 0.14);
  }
  * { margin: 0; padding: 0; box-sizing: border-box; }
  html, body {
    width: 1200px; height: 900px; overflow: hidden;
    background: var(--stage);
  }
  .stage { position: relative; width: 1200px; height: 900px; }
  .card {
    position: absolute; top: 271px;
    width: 457px; height: 281px;
    border-radius: 14px; overflow: hidden;
  }
  .card--front { left: 137px; background: var(--paper); }
  .card--back {
    left: 626px;
    background: linear-gradient(180deg, var(--brand-blue-light) 0%, var(--brand-blue-dark) 100%);
  }
  .corner-glow {
    position: absolute; right: 0; bottom: 0;
    width: 230px; height: 170px;
  }
  .card--front .corner-glow {
    background: radial-gradient(circle at 100% 100%, var(--soft-blue) 0%, rgba(120,165,205,0.12) 55%, rgba(255,255,255,0) 80%);
  }
  .card--back .corner-glow {
    background: radial-gradient(circle at 100% 100%, var(--soft-white) 0%, rgba(255,255,255,0.05) 55%, rgba(255,255,255,0) 80%);
  }
  .holder-name {
    position: absolute; left: 30px; top: 28px;
    font-family: "Exo 2", sans-serif; font-weight: 700;
    font-size: 15px; line-height: 19px; letter-spacing: 0.2px;
    color: var(--brand-blue); text-transform: uppercase;
  }
  .holder-role {
    position: absolute; left: 30px; top: 68px;
    font-family: "Carlito", sans-serif; font-size: 13px; line-height: 17px;
    color: var(--text-grey);
  }
  .wordmark {
    position: absolute;
    font-family: "Carlito", sans-serif; font-weight: 400;
    white-space: nowrap;
  }
  .card--front .wordmark {
    right: 30px; top: 100px; font-size: 25px; color: var(--brand-blue);
  }
  .card--back .wordmark {
    left: 0; right: 0; top: 166px; text-align: center;
    font-size: 29px; color: var(--paper);
  }
  .contact-list {
    position: absolute; left: 30px; top: 154px; list-style: none;
    font-family: "Carlito", sans-serif; font-size: 14px; color: var(--text-grey);
  }
  .contact-list li { display: flex; align-items: center; height: 21px; }
  .contact-icon { width: 14px; height: 14px; margin-right: 9px; flex: none; }
  .address {
    position: absolute; left: 30px; top: 227px;
    font-family: "Carlito", sans-serif; font-size: 14px; line-height: 17px;
    color: var(--text-grey); font-style: normal;
  }
</style>
</head>
<body>
<main class="stage">
  <section class="card card--front" aria-label="Voorkant visitekaartje">
    <div class="corner-glow" role="img" aria-label="Zachte blauwe decoratie in de hoek"></div>
    <h1 class="holder-name">Dr. Femke Voskuilen-<br>ter Horst</h1>
    <p class="holder-role">Psychiater/kinder-<br>en jeugdpsychiater</p>
    <p class="wordmark">Praktijk Voskuilen</p>
    <ul class="contact-list">
      <li>
        <svg class="contact-icon" viewBox="0 0 14 14" aria-hidden="true">
          <circle cx="7" cy="7" r="7" fill="#1f6cae"/>
          <path d="M4 5.2h6v1.2H4zM5 6.4h4l.8 3H4.2z" fill="#fff"/>
        </svg>
        06-58190274
      </li>
      <li>
        <svg class="contact-icon" viewBox="0 0 14 14" aria-hidden="true">
          <circle cx="7" cy="7" r="7" fill="#1f6cae"/>
          <rect x="3.8" y="4.8" width="6.4" height="4.4" fill="#fff"/>
          <path d="M3.8 4.8L7 7.4l3.2-2.6" fill="none" stroke="#1f6cae" stroke-width="0.8"/>
        </svg>
        info@praktijkvoskuilen-voorbeeld.nl
      </li>
      <li>
        <svg class="contact-icon" viewBox="0 0 14 14" aria-hidden="true">
          <circle cx="7" cy="7" r="7" fill="#1f6cae"/>
          <circle cx="7" cy="7" r="3.4" fill="none" stroke="#fff" stroke-width="1"/>
          <path d="M3.6 7h6.8M7 3.6v6.8" stroke="#fff" stroke-width="0.8"/>
        </svg>
        www.praktijkvoskuilen-voorbeeld.nl
      </li>
    </ul>
    <address class="address">Gerrit Wassinkstraat 4<br>3063 TW Rotterdam</address>
  </section>

  <section class="card card--back" aria-label="Achterkant visitekaartje">
    <div class="corner-glow" role="img" aria-label="Zachte lichte decoratie in de hoek"></div>
    <p class="wordmark">Praktijk Voskuilen</p>
  </section>
</main>
</body>
</html>
```